Management Company for Associations needs new and improved letterhead

We need a design for letterhead that looks professional. We like designs that can incorporate a lot of space for our letters, a new age professional font, and different styles to choose from. Please use the language in the attached letterhead example. The BRV logo needs to be incorporated in the letterhead; please follow the size requirements for use. We are trying to totally revamp our letterhead.
Industry/Entity Type
Property Management
Font styles to use
Serif
Script
Colors
ec1f27
Requirements
Must have
- BRV Logo in black, Q7 logo, Using both Top & Bottom, Red Color used to match logo color.
Nice to have
- (1 design with a watermark using Q7 logo)

```html
<!DOCTYPE html>
<html lang="en">
<head>
<meta charset="utf-8">
<title>Q7 Letterhead</title>
<link rel="stylesheet" href="https://fonts.googleapis.com/css2?family=Source+Sans+3:wght@400;600;700&display=swap">
<style>
  :root {
    --backdrop: #e9d3d0;
    --paper: #ffffff;
    --brand-red: #ec1f27;
    --deep-red: #8e1a1e;
    --ink: #1e1e1e;
    --muted: #6b6b6b;
    --rule-grey: #a9a9a9;
    --watermark: #f4e3df;
  }
  html, body {
    margin: 0;
    width: 1200px;
    height: 784px;
    overflow: hidden;
    background: var(--backdrop);
    font-family: "Source Sans 3", "Helvetica Neue", Arial, sans-serif;
  }
  .letterhead {
    position: absolute;
    left: 340px;
    top: 24px;
    width: 520px;
    height: 736px;
    background: var(--paper);
    overflow: hidden;
    box-shadow: 0 2px 8px rgba(0,0,0,0.12);
  }
  /* header */
  .header-rule-grey {
    position: absolute;
    top: 24px;
    height: 4px;
    background: linear-gradient(180deg, #d6d6d6, var(--rule-grey));
  }
  .header-rule-grey.left { left: 0; width: 24px; }
  .header-rule-grey.right { right: 0; width: 24px; }
  .header-rule-main {
    position: absolute;
    top: 24px;
    left: 190px;
    width: 250px;
    height: 4px;
    background: var(--ink);
  }
  .header-rule-main::after {
    content: "";
    position: absolute;
    left: 0; right: 0; top: 4px;
    height: 2px;
    background: var(--brand-red);
  }
  .partner-mark {
    position: absolute;
    left: 32px;
    top: 10px;
    display: flex;
    align-items: center;
    gap: 8px;
    font-size: 26px;
    font-weight: 600;
    color: var(--ink);
    letter-spacing: 1px;
  }
  .partner-mark .badge {
    width: 14px;
    height: 14px;
    background: var(--ink);
  }
  .brand-mark {
    position: absolute;
    left: 446px;
    top: 11px;
    display: flex;
    align-items: center;
    gap: 5px;
    font-size: 22px;
    font-weight: 700;
    color: var(--brand-red);
  }
  .brand-mark .dot {
    width: 12px;
    height: 12px;
    border-radius: 50%;
    background: var(--brand-red);
  }
  /* watermark */
  .watermark {
    position: absolute;
    left: 160px;
    top: 460px;
    width: 250px;
    height: 250px;
  }
  .watermark .ring {
    position: absolute;
    inset: 0;
    border-radius: 50%;
    border: 10px solid var(--watermark);
  }
  .watermark .name {
    position: absolute;
    inset: 0;
    display: flex;
    align-items: center;
    justify-content: center;
    font-size: 120px;
    font-weight: 700;
    color: var(--watermark);
  }
  /* footer */
  .footer-rule {
    position: absolute;
    left: 0; right: 0; bottom: 0;
    height: 6px;
    background: var(--deep-red);
    border-top: 2px solid var(--brand-red);
  }
  .contact-list {
    position: absolute;
    left: 12px;
    right: 12px;
    bottom: 18px;
    margin: 0;
    padding: 0;
    list-style: none;
    display: flex;
    justify-content: space-between;
    align-items: flex-end;
    font-size: 9px;
    line-height: 1.2;
    color: var(--muted);
  }
  .contact-item {
    display: flex;
    flex-direction: column;
    align-items: center;
    gap: 5px;
    white-space: nowrap;
  }
  .contact-item svg { width: 10px; height: 10px; }
</style>
</head>
<body>
  <main class="letterhead">
    <header>
      <div class="header-rule-grey left"></div>
      <div class="partner-mark"><span class="badge"></span>BRV</div>
      <div class="header-rule-main"></div>
      <div class="brand-mark"><span class="dot"></span>Q7</div>
      <div class="header-rule-grey right"></div>
    </header>

    <div class="watermark" aria-hidden="true">
      <div class="ring"></div>
      <div class="name">Q7</div>
    </div>

    <footer>
      <ul class="contact-list">
        <li class="contact-item address">
          <svg viewBox="0 0 10 10"><circle cx="5" cy="5" r="4.3" fill="none" stroke="#ec1f27" stroke-width="1"/><path d="M5 2.5a1.6 1.6 0 0 1 1.6 1.6C6.6 5.4 5 7.5 5 7.5S3.4 5.4 3.4 4.1A1.6 1.6 0 0 1 5 2.5z" fill="#ec1f27"/></svg>
          <span>000 North Lake St., Suite 300, Linden, US 0000</span>
        </li>
        <li class="contact-item phone">
          <svg viewBox="0 0 10 10"><circle cx="5" cy="5" r="4.3" fill="none" stroke="#ec1f27" stroke-width="1"/><path d="M3.4 2.8l1 .9-.5.8c.3.7.9 1.3 1.6 1.6l.8-.5.9 1-.6.8C5 7.3 2.7 5 2.6 3.4z" fill="#ec1f27"/></svg>
          <span>000.999.0000</span>
        </li>
        <li class="contact-item fax">
          <svg viewBox="0 0 10 10"><circle cx="5" cy="5" r="4.3" fill="none" stroke="#ec1f27" stroke-width="1"/><rect x="3" y="3.8" width="4" height="2.6" fill="#ec1f27"/><rect x="3.7" y="2.6" width="2.6" height="1.2" fill="#ec1f27"/></svg>
          <span>000.441.0000</span>
        </li>
        <li class="contact-item email">
          <svg viewBox="0 0 10 10"><circle cx="5" cy="5" r="4.3" fill="none" stroke="#ec1f27" stroke-width="1"/><rect x="2.8" y="3.4" width="4.4" height="3.2" fill="none" stroke="#ec1f27" stroke-width="0.8"/><path d="M2.8 3.4L5 5.2l2.2-1.8" fill="none" stroke="#ec1f27" stroke-width="0.8"/></svg>
          <span>example@example.com</span>
        </li>
        <li class="contact-item web">
          <svg viewBox="0 0 10 10"><circle cx="5" cy="5" r="4.3" fill="none" stroke="#ec1f27" stroke-width="1"/><circle cx="5" cy="5" r="2.2" fill="none" stroke="#ec1f27" stroke-width="0.8"/><path d="M2.8 5h4.4M5 2.8v4.4" stroke="#ec1f27" stroke-width="0.6"/></svg>
          <span>www.example.com</span>
        </li>
      </ul>
      <div class="footer-rule"></div>
    </footer>
  </main>
</body>
</html>
```